Re-vamp existing website :www.tallowmerefinch.com.au

We need a new website design for this website
www.tallowmerefinch.com.au.

"creating financial lightbulb moments"

Looking for something modern, corporate like this https://www.pebbleharbor.com.au

Imagery is important, showing really great images of what we do.

We want to keep the theme of:
Build Your Future
Invest in your Dreams
Grow You

We want a blog/opinion page on the website

Staying with our three logo colours throughout

Industry/Entity Type

Financial Service

Number of Pages Required

5+ page

```html
<!DOCTYPE html>
<html lang="en">
<head>
<meta charset="utf-8">
<title>Tallowmere Finch Financial Group</title>
<link rel="stylesheet" href="https://fonts.googleapis.com/css2?family=Open+Sans:wght@300;400;600;700&display=swap">
<style>
:root{
  --blue:#2aa9e0;
  --green:#8cc63f;
  --ink:#444;
  --muted:#8a8a8a;
  --band:#dcdcdc;
  --footer:#2b2b2b;
  --footer-base:#1f1f1f;
  --white:#fff;
}
*{box-sizing:border-box;margin:0;padding:0}
html,body{width:1200px;height:2406px;overflow:hidden}
body{position:relative;background:var(--white);font-family:"Open Sans",Arial,sans-serif;color:var(--ink)}
.abs{position:absolute}

/* header */
.brand{left:0;top:0;width:300px;height:136px;background:var(--white);display:flex;align-items:center;gap:14px;padding-left:74px}
.brand-dot{width:40px;height:40px;border-radius:50%;background:var(--blue);flex:none}
.brand-name{font-size:22px;font-weight:700;color:var(--blue);line-height:1.1}
.topbar{left:300px;top:0;width:900px;height:136px;background:var(--blue);color:var(--white)}
.contact-row{position:absolute;right:75px;top:10px;display:flex;align-items:center;gap:16px;font-size:19px}
.contact-row span{display:flex;align-items:center;gap:10px}
.contact-row .divider{width:1px;height:28px;background:rgba(255,255,255,.5)}
.topbar-rule{position:absolute;left:0;right:75px;top:48px;height:1px;background:rgba(255,255,255,.55)}
.main-nav{position:absolute;left:47px;top:81px;display:flex;gap:54px;font-size:15px;font-weight:600}
.search-icon{position:absolute;right:77px;top:84px}

/* hero */
.hero{left:0;top:136px;width:1200px;height:441px;background:linear-gradient(100deg,#c9c2b8 0%,#8d7c6f 30%,#b5aaa0 55%,#6d7480 75%,#d8dde2 100%)}
.hero-title{left:75px;top:337px;height:67px;padding:0 14px;background:rgba(42,120,150,.55);color:var(--white);font-size:70px;font-weight:300;line-height:67px}

/* about */
.about-heading{left:83px;top:636px;font-size:38px;font-weight:600;color:#3d3d3d}
.about-lead{left:75px;top:694px;width:530px;font-size:28px;font-weight:300;line-height:38px;color:#555}
.about-rule{left:75px;top:841px;width:515px;height:2px;background:#ccc}
.about-rule::before{content:"";position:absolute;left:0;top:0;width:86px;height:2px;background:var(--green)}
.about-body{left:83px;top:872px;width:505px;font-size:21px;line-height:33px;color:var(--muted)}
.btn-learn{left:75px;top:1031px;width:195px;height:52px;background:var(--blue);color:var(--white);font-size:21px;font-weight:600;display:flex;align-items:center;justify-content:center}
.about-photo{left:637px;top:645px;width:488px;height:438px;background:linear-gradient(135deg,#e8ecef,#c7d3dc 60%,#5b8fb8)}
.journey{left:0;top:1144px;width:1200px;text-align:center;font-size:37px;font-weight:600;color:#3d3d3d}

/* partners */
.partners{left:0;top:1232px;width:1200px;height:141px;background:var(--band);display:flex;align-items:center;justify-content:center;gap:28px}
.partner{background:#9a9a9a;opacity:.75}
.partner.wide{width:100px;height:22px}
.partner.box{width:90px;height:34px}
.partner.round{width:66px;height:66px;border-radius:50%}

/* blog */
.blog-heading{left:0;top:1436px;width:1200px;text-align:center;font-size:37px;font-weight:600;color:#3d3d3d}
.feature{left:75px;top:1519px;width:509px;height:488px;background:linear-gradient(135deg,#d9d3ca,#9c8d80 55%,#e2e4e6)}
.feature-caption{left:75px;top:1877px;width:509px;height:130px;background:rgba(60,60,60,.72);color:var(--white);padding:14px 26px}
.feature-caption h3{font-size:27px;font-weight:400;line-height:36px}
.feature-caption p{font-size:14px;line-height:19px;margin-top:6px}
.post-thumb{width:170px;height:134px;background:linear-gradient(135deg,#cfcac4,#8c8580 60%,#d8dadc)}
.post-body{width:314px}
.post-title{font-size:20px;color:#555;line-height:26px;white-space:nowrap}
.post-excerpt{font-size:12.5px;line-height:18px;color:var(--muted);margin-top:6px}
.post-meta{position:absolute;left:0;top:91px;width:314px;height:37px;background:#eee;display:flex;align-items:center;padding:0 12px;gap:30px;font-size:13px;color:#b5b5b5}
.post-meta span{display:flex;align-items:center;gap:8px}
.post-meta .share{margin-left:auto}

/* footer */
.footer{left:0;top:2060px;width:1200px;height:290px;background:var(--footer);color:#ddd}
.footer h4{position:absolute;top:39px;font-size:15px;font-weight:400;letter-spacing:.5px;color:#eee}
.contact-item{position:absolute;left:96px;display:flex;gap:20px;font-size:13.5px;line-height:19px}
.contact-item svg{flex:none;margin-top:2px}
.quick-links{position:absolute;left:417px;top:93px;list-style:none;font-size:13.5px;line-height:31px}
.map{position:absolute;left:611px;top:96px;width:241px;height:151px;background:linear-gradient(135deg,#efe7d3,#e2d8c2);border:3px solid #fff}
.award-badge{position:absolute;left:954px;top:37px;width:104px;height:104px;border-radius:50%;background:#e9b719;border:4px solid #c79a0e}
.award-text{position:absolute;left:925px;top:157px;width:220px;font-size:19px;line-height:31px;font-weight:300;color:#eee}
.footer-base{left:0;top:2350px;width:1200px;height:56px;background:var(--footer-base);color:#ccc;font-size:13px;display:flex;align-items:center;padding:0 75px}
.social-dot{margin-left:auto;width:14px;height:14px;border-radius:50%;background:#3a78c2}
</style>
</head>
<body>

<header>
  <div class="abs brand">
    <span class="brand-dot"></span>
    <span class="brand-name">Tallowmere<br>Finch</span>
  </div>
  <div class="abs topbar">
    <div class="contact-row">
      <span>
        <svg width="18" height="18" viewBox="0 0 24 24" fill="#fff"><path d="M6.6 10.8a15 15 0 0 0 6.6 6.6l2.2-2.2a1 1 0 0 1 1-.25 11.4 11.4 0 0 0 3.6.57 1 1 0 0 1 1 1V20a1 1 0 0 1-1 1A17 17 0 0 1 3 4a1 1 0 0 1 1-1h3.5a1 1 0 0 1 1 1c0 1.25.2 2.45.57 3.57a1 1 0 0 1-.25 1z"/></svg>
        +0400 555 019
      </span>
      <span class="divider"></span>
      <span>
        <svg width="20" height="14" viewBox="0 0 20 14" fill="#fff"><path d="M0 0h20v14H0z" fill-opacity=".9"/><path d="M0 0l10 8 10-8" stroke="#2aa9e0" stroke-width="1.6" fill="none"/></svg>
        theteam@tallowmerefinch.com.au
      </span>
    </div>
    <div class="topbar-rule"></div>
    <nav class="main-nav">
      <span>Home</span><span>About Us</span><span>Home Loans</span><span>Business Lending</span><span>Contact Us</span>
    </nav>
    <svg class="search-icon" width="20" height="20" viewBox="0 0 20 20" fill="none" stroke="#fff" stroke-width="2"><circle cx="8" cy="8" r="6"/><path d="M12.5 12.5L18 18"/></svg>
  </div>
</header>

<section>
  <div class="abs hero" role="img" aria-label="Photo of three smiling professionals discussing plans over a tablet"></div>
  <h1 class="abs hero-title">Bulid Your Future</h1>
</section>

<section>
  <h2 class="abs about-heading">About us</h2>
  <p class="abs about-lead">At Tallowmere Finch our team is on the road everyday and we're able to come to you at your preferred location.</p>
  <div class="abs about-rule"></div>
  <p class="abs about-body">Everyone has financial goals but most might need some help in the steps getting there. Let me help by making sure your structure is in line with your goals.</p>
  <div class="abs btn-learn">Learn More</div>
  <div class="abs about-photo" role="img" aria-label="Photo of hands reviewing a printed bar chart with a pen"></div>
  <h2 class="abs journey">Click Here to start your Journey!</h2>
</section>

<section class="abs partners" aria-label="Lending partners">
  <span class="partner wide"></span>
  <span class="partner box"></span>
  <span class="partner box"></span>
  <span class="partner box" style="width:60px;height:60px"></span>
  <span class="partner round"></span>
  <span class="partner wide"></span>
  <span class="partner round" style="width:50px;height:50px"></span>
  <span class="partner wide" style="width:90px;height:34px"></span>
  <span class="partner wide"></span>
</section>

<section>
  <h2 class="abs blog-heading">Our Blog</h2>
  <div class="abs feature" role="img" aria-label="Photo of colleagues looking at a laptop together"></div>
  <div class="abs feature-caption">
    <h3>Lorem ipsum dolor sit amet consec</h3>
    <p>sit amet, consectetur adipiscing elit. Phasellus semper elementum vestibulum. Cras posuere dictum quam quis tempus. Proin a metus</p>
  </div>

  <div class="abs post-thumb" style="left:611px;top:1519px" role="img" aria-label="Photo of a business handshake"></div>
  <div class="abs post-body" style="left:810px;top:1510px;height:128px">
    <h3 class="post-title">Lorem ipsum dolor sit amet consec</h3>
    <p class="post-excerpt">sit amet, consectetur adipiscing elit. Phasellus semper elementum vestibulum. Cras posuere dictum quam quis tempus. Proin a metus massa.</p>
    <div class="post-meta"><span>&#9829; 150</span><span>&#9632; 20</span><span class="share">&lt;</span></div>
  </div>

  <div class="abs post-thumb" style="left:611px;top:1690px" role="img" aria-label="Photo of a woman working at a desk"></div>
  <div class="abs post-body" style="left:810px;top:1682px;height:128px">
    <h3 class="post-title">Lorem ipsum dolor sit amet consec</h3>
    <p class="post-excerpt">sit amet, consectetur adipiscing elit. Phasellus semper elementum vestibulum. Cras posuere dictum quam quis tempus. Proin a metus massa.</p>
    <div class="post-meta"><span>&#9829; 150</span><span>&#9632; 20</span><span class="share">&lt;</span></div>
  </div>

  <div class="abs post-thumb" style="left:611px;top:1873px" role="img" aria-label="Photo of a smiling couple"></div>
  <div class="abs post-body" style="left:810px;top:1864px;height:128px">
    <h3 class="post-title">Lorem ipsum dolor sit amet consec</h3>
    <p class="post-excerpt">sit amet, consectetur adipiscing elit. Phasellus semper elementum vestibulum. Cras posuere dictum quam quis tempus. Proin a metus massa.</p>
    <div class="post-meta"><span>&#9829; 150</span><span>&#9632; 20</span><span class="share">&lt;</span></div>
  </div>
</section>

<footer>
  <div class="abs footer">
    <h4 style="left:96px">CONTACTS</h4>
    <div class="contact-item" style="top:93px">
      <svg width="12" height="16" viewBox="0 0 12 16" fill="#fff"><path d="M6 0a6 6 0 0 0-6 6c0 4.5 6 10 6 10s6-5.5 6-10a6 6 0 0 0-6-6zm0 8.5A2.5 2.5 0 1 1 6 3.5a2.5 2.5 0 0 1 0 5z"/></svg>
      <span>Suite 4, Level 3<br>15-17 Wren Street Marlow NSW 2290</span>
    </div>
    <div class="contact-item" style="top:158px">
      <svg width="14" height="14" viewBox="0 0 24 24" fill="#fff"><path d="M6.6 10.8a15 15 0 0 0 6.6 6.6l2.2-2.2a1 1 0 0 1 1-.25 11.4 11.4 0 0 0 3.6.57 1 1 0 0 1 1 1V20a1 1 0 0 1-1 1A17 17 0 0 1 3 4a1 1 0 0 1 1-1h3.5a1 1 0 0 1 1 1c0 1.25.2 2.45.57 3.57a1 1 0 0 1-.25 1z"/></svg>
      <span>0400 555 019</span>
    </div>
    <div class="contact-item" style="top:210px">
      <svg width="14" height="10" viewBox="0 0 20 14"><path d="M0 0h20v14H0z" fill="#fff"/><path d="M0 0l10 8 10-8" stroke="#2b2b2b" stroke-width="1.6" fill="none"/></svg>
      <span>theteam@tallowmerefinch.com.au</span>
    </div>

    <h4 style="left:417px">QUICK LINKS</h4>
    <ul class="quick-links">
      <li>Home</li><li>About Us</li><li>Home Loans</li><li>Business Lending</li><li>Contact Us</li>
    </ul>

    <h4 style="left:611px">LOCATION</h4>
    <div class="map" role="img" aria-label="Street map showing the office location"></div>

    <div class="award-badge" role="img" aria-label="Industry award badge"></div>
    <p class="award-text">Lender Insight Weekly Top 30 Rising Broker in Australia</p>
  </div>
  <div class="abs footer-base">
    <span>Copyright © . All Rights Reserved</span>
    <span class="social-dot"></span>
  </div>
</footer>

</body>
</html>
```